Real Estate Agent Business Card Needs a New Eye Catching Design

Looking for a designer that can revamp a current business card.
Looking for something with a lot more style.
Something that will catch the eye

Included in the file:
The old business card. (Old Business Card)
A new place holder image to be used as headshot. (Temp Headshot)
Homeward KT Logo (KT logo)
Open Residence Pledge Logo (RP logo)

The working PSD file will need to be delivered with the individual layers separated and edible. (I'll being changing the new headshot later)
Any fonts used also need to be delivered.

Overall, the old business card has the elements but in a horrible state.
If you have any questions, please feel free to reach out.

Thank you

Glen

Target Market(s)

Individuals want to either sale or buy a home

Industry/Entity Type

Real Estate Agent

Design Requirements:
Headshot needs to be a head and shoulders and have a transparent background.

The American Flag should implemented into the design somehow.

Both the KT logo and RP logo need to be incorporated.

All information on the OLD Business Card should be included.

Requirements
Must have
• Transparent head shot set against the final background
• American Flag and/or colors-theme incorporated
• KT logo and RP logo incorporated

```html
<!DOCTYPE html>
<html lang="en">
<head>
<meta charset="utf-8">
<title>Liberty Ridge Realty – Business Card</title>
<link rel="stylesheet" href="https://fonts.googleapis.com/css2?family=Jost:wght@400&family=Roboto:wght@400;500;700&display=swap">
<style>
  :root {
    --page: #e4e4e4;
    --navy: #373270;
    --salmon: #dc8a5f;
    --flag-red: #e0202d;
    --white: #ffffff;
    --ink: #111111;
  }
  * { box-sizing: border-box; margin: 0; padding: 0; }
  html, body { width: 1200px; height: 830px; overflow: hidden; }
  body { background: var(--page); font-family: "Roboto", sans-serif; position: relative; }

  .card {
    position: absolute; left: 100px; top: 129px;
    width: 1000px; height: 572px;
    background: var(--white);
    box-shadow: 0 2px 6px rgba(0,0,0,.25);
    overflow: hidden;
  }
  .info-panel {
    position: absolute; left: 0; top: 0; width: 524px; height: 100%;
    background: var(--navy); color: var(--white);
  }
  .flag-stripes {
    position: absolute; left: 524px; top: 0; width: 26px; height: 100%;
    background: linear-gradient(to right,
      var(--white) 0 2px, var(--flag-red) 2px 7px, var(--white) 7px 11px,
      var(--flag-red) 11px 16px, var(--white) 16px 20px, var(--flag-red) 20px 25px,
      var(--white) 25px 26px);
  }
  .company-name {
    position: absolute; left: 46px; top: 104px;
    font-family: "Jost", sans-serif; font-weight: 400;
    font-size: 43px; color: var(--salmon); letter-spacing: 0; white-space: nowrap;
  }
  .agent-name {
    position: absolute; left: 45px; top: 212px;
    font-weight: 700; font-size: 37px; color: var(--salmon);
  }
  .agent-title {
    position: absolute; left: 47px; top: 256px;
    font-weight: 500; font-size: 25px;
  }
  .address {
    position: absolute; left: 47px; top: 298px;
    font-size: 24px; line-height: 31px; font-style: normal;
  }
  .contact-list {
    position: absolute; left: 47px; top: 373px; list-style: none;
  }
  .contact-list li {
    display: flex; align-items: center; height: 31.5px;
    font-size: 24px;
  }
  .contact-list svg { width: 24px; height: 24px; margin-right: 14px; flex: none; }
  .contact-list svg * { fill: var(--salmon); }

  .headshot {
    position: absolute; left: 661px; top: 123px; width: 227px; height: 272px;
    border: 1px solid #555; border-radius: 24px;
    background: linear-gradient(180deg, #f1f0ee 0%, #e6e2dd 55%, #2c2c3a 100%);
  }
  .badges {
    position: absolute; left: 666px; top: 427px; width: 216px; height: 64px;
    display: flex; align-items: center; justify-content: space-between;
  }
  .badge {
    display: flex; align-items: center; gap: 6px;
    font-family: "Roboto", sans-serif; font-weight: 700; color: var(--ink);
  }
  .badge-square { width: 20px; height: 20px; background: var(--ink); flex: none; }
  .badge-kt { font-size: 15px; white-space: nowrap; }
  .badge-rp { font-size: 10px; line-height: 12px; width: 70px; }
</style>
</head>
<body>
  <section class="card">
    <div class="info-panel">
      <h1 class="company-name">LIBERTY RIDGE REALTY</h1>
      <h2 class="agent-name">Dana Morrow</h2>
      <p class="agent-title">SALES AGENT</p>
      <address class="address">2870 W. Canyon Road<br>Sagebrook, NV 89110</address>
      <ul class="contact-list">
        <li>
          <svg viewBox="0 0 24 24" aria-hidden="true"><path d="M6.6 10.8a15.2 15.2 0 0 0 6.6 6.6l2.2-2.2c.3-.3.7-.4 1-.2 1.1.4 2.3.6 3.6.6.6 0 1 .4 1 1V20c0 .6-.4 1-1 1A17 17 0 0 1 3 4c0-.6.4-1 1-1h3.5c.6 0 1 .4 1 1 0 1.3.2 2.5.6 3.6.1.3 0 .7-.2 1z"/></svg>
          555 - 201 - 4478
        </li>
        <li>
          <svg viewBox="0 0 24 24" aria-hidden="true"><path d="M7 1h10a2 2 0 0 1 2 2v18a2 2 0 0 1-2 2H7a2 2 0 0 1-2-2V3a2 2 0 0 1 2-2zm0 3v15h10V4z"/></svg>
          555-318-2290
        </li>
        <li>
          <svg viewBox="0 0 24 24" aria-hidden="true"><path d="M7 3h10v5H7z"/><path d="M2 9h20v9h-3v-4H5v4H2z"/><path d="M6 15h12v6H6z"/></svg>
          555-318-2291
        </li>
        <li>
          <svg viewBox="0 0 24 24" aria-hidden="true"><path d="M2 5h20v2l-10 6L2 7z"/><path d="M2 9l10 6 10-6v10H2z"/></svg>
          homes@libertyridge.example
        </li>
      </ul>
    </div>
    <div class="flag-stripes"></div>

    <div class="headshot" role="img" aria-label="Head-and-shoulders portrait of the agent"></div>

    <div class="badges">
      <div class="badge badge-kt"><span class="badge-square"></span>Homeward KT</div>
      <div class="badge badge-rp">Open Residence Pledge</div>
    </div>
  </section>
</body>
</html>
```